Help us to design our 2015 circus poster

We are Morrow's Circus, a 1920s themed travelling circus. We have a very specific brief for this poster, but you have total freedom to choose how to implement it:

1. The logo of Morrow's Circus must be VERY clear and prominent on the poster. Especially the word circus. Perhaps you could give a border to each letter to help it stand out?

2. It must look like a lot of fun for children aged 3-14. Pictures or illustrations of children smiling and laughing while watching a show would work well but it is really up to you how to deliver this objective.

3. We are a 1920s experience and so the poster needs to have a vintage theme to it. Have a look at the way 'Pelham's Fun Fair' make their posters and you will see what I mean.

4. At least one third of the space on the poster must be dedicated to the location and timing of the event. For now, use the following data:

Brookvale Green, St Albans, AL7 3QN
28th March - 6th April 2015

5. Include the promotion: EASTER SPECIAL: KIDS GO FREE!*
*One free child ticket with every full priced adult ticket purchased.

6. Include the following telephone number: 01727 555 813 in a very prominent location

7. Include the website address: www.morrowsbigtop.example

8. Use VERY bright colours. The posters need to reall stand out when they are in shop windows. The words circus and the offer "Kids go free" must really jump out of the page and stop people as they are walking past.

Target Market(s)

The show is a family show. But it is mums aged 18-40 that decide to buy the tickets for their children so make sure that the poster makes the event look like a lot of fun for children. Pictures of laughing children or children having fun would work but it must be clear that we are a circus show. If you have a look at www.facebook.com/morrowsbigtop you will see a video which has a lot of children enjoying our show. That's the feeling I want to capture in the poster.

Industry/Entity Type

Adult

Colors
ec2027
fbed22
f79020
9bcb3c
e24197

Requirements
Must have
• See project description
Nice to have
• The vintage feel of Pelham's Fun Fair posters (have a look on Google Images). Also the clarity with which they communicate the event information (dates/times etc.)

```html
<!DOCTYPE html>
<html lang="en">
<head>
<meta charset="utf-8">
<title>Morrow's Circus – Easter 2015</title>
<link href="https://fonts.googleapis.com/css2?family=Anton&family=Arimo:wght@700&family=Archivo+Narrow:wght@500&display=swap" rel="stylesheet">
<style>
  :root {
    --yellow: #fbed22;
    --yellow-soft: #fff7a8;
    --red: #e2383f;
    --red-deep: #ec2027;
    --teal: #14a7a4;
    --teal-dark: #0c7f7d;
    --ink: #111111;
    --white: #ffffff;
  }
  html, body { margin: 0; padding: 0; overflow: hidden; background: var(--white); }
  .poster {
    position: relative;
    width: 849px;
    height: 1200px;
    overflow: hidden;
    background: radial-gradient(ellipse at 50% 55%, var(--yellow-soft) 0%, var(--yellow) 60%, #f7e01a 100%);
    font-family: "Arimo", Arial, sans-serif;
  }
  .bunting {
    position: absolute; left: 0; top: 0; width: 849px; height: 28px;
    background: linear-gradient(180deg, var(--red) 0%, var(--teal) 100%);
    opacity: .85;
  }
  .ribbon { position: absolute; left: 0; top: 36px; width: 849px; height: 100px; }
  .ribbon__text {
    position: absolute; left: 70px; top: 42px; width: 709px; height: 80px;
    display: flex; align-items: center; justify-content: center;
    white-space: nowrap;
    font-family: "Anton", Impact, sans-serif;
    font-size: 40px; line-height: 1; color: var(--yellow);
    transform: scale(0.84, 1.3);
    transform-origin: center;
  }
  .logo {
    position: absolute; left: 0; top: 118px; width: 849px; margin: 0;
    text-align: center; color: var(--red); font-weight: 700;
    line-height: 1;
  }
  .logo__name { display: block; font-size: 92px; }
  .logo__word { display: block; font-size: 178px; letter-spacing: 4px; margin-top: 10px; }
  .flourish {
    position: absolute; top: 155px; width: 90px; height: 40px;
    background: linear-gradient(90deg, var(--teal), var(--red));
    border-radius: 4px;
  }
  .flourish--left { left: 92px; }
  .flourish--right { left: 678px; }
  .tent {
    position: absolute; left: 0; top: 470px; width: 849px; height: 246px;
    background: linear-gradient(180deg, rgba(226,56,63,0) 0%, #f0a33a 30%, var(--red) 100%);
    clip-path: polygon(0 90%, 20% 45%, 50% 0, 80% 45%, 100% 90%, 100% 100%, 0 100%);
  }
  .offer-arrow { position: absolute; left: 22px; top: 402px; width: 380px; height: 84px; }
  .offer-arrow__text {
    position: absolute; left: 40px; top: 423px; width: 305px;
    font-size: 31px; color: var(--white); font-family: Arial, "Arimo", sans-serif; font-weight: 400;
    letter-spacing: .5px;
  }
  .offer-kids {
    position: absolute; left: 437px; top: 418px;
    font-size: 43px; color: var(--teal); font-weight: 700;
  }
  .offer-free {
    position: absolute; left: 640px; top: 412px; width: 188px; height: 72px;
    background: var(--ink); transform: rotate(-13deg);
    display: flex; align-items: center; justify-content: center;
    font-size: 62px; color: var(--red-deep); font-weight: 700; letter-spacing: 1px;
    border-radius: 4px;
  }
  .offer-terms {
    position: absolute; left: 606px; top: 503px; width: 226px; margin: 0;
    font-family: "Archivo Narrow", "Arial Narrow", sans-serif; font-size: 14.5px;
    line-height: 14px; color: var(--ink); text-align: center;
  }
  .info {
    position: absolute; left: 12px; top: 724px; width: 826px; height: 358px;
    background: var(--white);
    box-sizing: border-box;
    border-top: 6px dotted var(--teal);
    text-align: center; color: var(--ink);
  }
  .info__venue { margin: 24px 0 0; font-size: 65px; line-height: 66px; font-weight: 700; }
  .info__dates { margin: 2px 0 0; font-size: 49px; line-height: 54px; font-weight: 700; }
  .info__booking {
    display: flex; justify-content: space-between; align-items: baseline;
    margin: 0 68px 0 78px; line-height: 52px; color: var(--red); font-weight: 700;
  }
  .info__book { font-size: 47px; letter-spacing: 1px; }
  .info__phone { font-size: 41px; }
  .info__web { margin: 0; font-size: 41px; line-height: 42px; color: var(--red); font-weight: 700; }
  .audience {
    position: absolute; left: 0; top: 1082px; width: 849px; height: 118px;
    background: linear-gradient(180deg, #d9a26a 0%, #7d5a9a 55%, var(--red) 100%);
  }
</style>
</head>
<body>
<main class="poster">
  <div class="bunting" role="img" aria-label="Row of coloured bunting flags"></div>

  <svg class="ribbon" viewBox="0 0 849 100" aria-hidden="true">
    <polygon points="20,28 100,28 100,100 20,100 50,64" fill="var(--teal)"/>
    <polygon points="829,28 749,28 749,100 829,100 799,64" fill="var(--teal)"/>
    <polygon points="70,90 100,100 100,90" fill="var(--teal-dark)"/>
    <polygon points="779,90 749,100 749,90" fill="var(--teal-dark)"/>
    <rect x="70" y="4" width="709" height="86" fill="var(--teal)"/>
  </svg>
  <div class="ribbon__text">★ALL HUMAN VINTAGE EXTRAVAGANZA★</div>

  <div class="flourish flourish--left" role="img" aria-label="Star and pennant ornament"></div>
  <div class="flourish flourish--right" role="img" aria-label="Star and pennant ornament"></div>

  <h1 class="logo">
    <span class="logo__name">Morrow's</span>
    <span class="logo__word">CIRCUS</span>
  </h1>

  <div class="tent" role="img" aria-label="Red and yellow striped big top circus tent with flags"></div>

  <svg class="offer-arrow" viewBox="0 0 380 84" aria-hidden="true">
    <polygon points="4,16 290,16 290,2 376,42 290,82 290,68 4,68" fill="var(--white)"/>
    <polygon points="9,21 295,21 295,11 366,42 295,73 295,63 9,63" fill="var(--teal)"/>
  </svg>
  <div class="offer-arrow__text">EASTER SPECIAL</div>
  <div class="offer-kids">KIDS GO</div>
  <div class="offer-free">FREE</div>
  <p class="offer-terms">One free child ticket with every full priced adult ticket purchased.</p>

  <section class="info">
    <p class="info__venue">Brookvale Green,<br>St Albans, AL7 3QN</p>
    <p class="info__dates">28th March - 6th April 2015</p>
    <div class="info__booking">
      <span class="info__book">BOOK NOW</span>
      <span class="info__phone">01727 555 813</span>
    </div>
    <p class="info__web">www.morrowsbigtop.example</p>
  </section>

  <div class="audience" role="img" aria-label="Illustrated audience of children and parents seen from behind, seated in red chairs"></div>
</main>
</body>
</html>
```